Leaf By Frost - Stationery Design Project

Hi everyone,

We need a business card and a stationary set designed for a new corporate video production company based in Sydney, 'Leaf By Frost'.

The name refers to the mythological 'phoenix' so we would like to see designs that are appropriate to both the name and to a creative film company. The key thing is, we need to appear fresh and creative while maintaining professionalism.

We would like to stick with dark colors for the basis of the card. One idea that came up was obsidian/volcanic rock with the logo cracking through to reveal lava or something fire like. This is just one idea that has come up, but we are of course open to others and would love to see what people can come up with. Extensive use of flames/fire imagery is not really what we are after.

Also, cinematic as opposed to corporate is preferable.

**** UPDATE ****
When I hand over the card to a prospective client, I want them to feel like they are receiving an obsidian plate with inscriptions in it (ie the phoenix). Looking for something elemental and rigid to contrast and complement the graceful lines of the logo.

Designs we require:
- Business card
(We would like a business card that makes use of some of the more premium business card printing options, such as foil stamping, embossing/debossing, painted edges, spot UV etc. Doesnt have to use all these things, only what you feel works, but we are looking for a business card that stands out and is memorable and these nice touches have that effect. For an example of what is possible, check out "http://www.glossvantage.example/base/category/business-card-gallery/".)

- Letter head
- With compliments slip
- Display folder

COPMPANY DETAILS:
ABN: 52 804 319 246
Company Address: 7/18-20 Hollin Ave, Kelmore NSW 2094
Name: Rob K. Deverill
Title: Producer
Contact Number: 0417 352 918
email: rob@leafbyfrost.example
website: www.leafbyfrost.example

ABOUT THE PHOENIX:
The phoenix is a musical bird from mythology, known for its long fancy tail and small plume on the top of its head. They are elegant and graceful and symbolize immortality, endurance and strength, believed to live for 5 centuries before they were reborn from their ashes.
Updates

Hi everyone,

We have just updated the design brief to include business contact information, website etc. should anyone require it for their designs.

Thanks

Rob

Target Market(s)

Other creative businesses and marketing firms.

Industry/Entity Type

Printing

Requirements
Must have
• Basic printing requirements:
- CMYK colour space
- 300dpi resolution
- Color bleed/crop marks etc to allow for trimming where necessary
- Source files upon handover
Should not have
• Overuse of fire/flame imagery

```html
<!DOCTYPE html>
<html lang="en">
<head>
<meta charset="utf-8">
<title>Leaf By Frost – Stationery Set</title>
<link rel="stylesheet" href="https://fonts.googleapis.com/css2?family=Cinzel:wght@400;600&family=Lato:wght@400;700&display=swap">
<style>
  :root{
    --backdrop:#acabac;
    --obsidian:#0b0d17;
    --slate:#3b4145;
    --paper:#e6e6e7;
    --paper-shade:#c9c9cb;
    --ember:#c8202a;
    --ink:#3a3a3e;
    --silver:#d9dadc;
    --mute:#8b8f95;
  }
  html,body{margin:0;padding:0;overflow:hidden;background:var(--backdrop);}
  .stationery-board{display:block;width:1200px;height:924px;}
  .wordmark{font-family:"Cinzel",serif;font-weight:400;fill:var(--silver);letter-spacing:3px;}
  .detail{font-family:"Lato",sans-serif;fill:var(--ink);}
  .detail-light{font-family:"Lato",sans-serif;fill:var(--mute);}
  .web{font-family:"Lato",sans-serif;font-weight:700;fill:var(--ember);}
  .holder-name{font-family:"Cinzel",serif;fill:var(--silver);}
  .mark-dot{fill:none;stroke:var(--ember);stroke-width:1.4;}
</style>
</head>
<body>
<svg class="stationery-board" viewBox="0 0 1200 924" xmlns="http://www.w3.org/2000/svg">
  <defs>
    <linearGradient id="obsidian-sheen" x1="0" y1="0" x2="1" y2="1">
      <stop offset="0" stop-color="#10131f"/>
      <stop offset="0.6" stop-color="#07080f"/>
      <stop offset="1" stop-color="#1a1e27"/>
    </linearGradient>
    <linearGradient id="slate-wave" x1="0" y1="0" x2="0" y2="1">
      <stop offset="0" stop-color="#12151f"/>
      <stop offset="1" stop-color="#464c4f"/>
    </linearGradient>
    <linearGradient id="paper-sheen" x1="0" y1="0" x2="1" y2="0">
      <stop offset="0" stop-color="#f4f4f4"/>
      <stop offset="1" stop-color="#dcdcde"/>
    </linearGradient>
    <linearGradient id="flap-sheen" x1="0" y1="0" x2="1" y2="0">
      <stop offset="0" stop-color="#bdbdc0"/>
      <stop offset="0.5" stop-color="#e9e9ea"/>
      <stop offset="1" stop-color="#f7f7f7"/>
    </linearGradient>
    <linearGradient id="card-gloss" x1="0" y1="0" x2="0" y2="1">
      <stop offset="0" stop-color="#2b2f3a"/>
      <stop offset="0.5" stop-color="#0d0f18"/>
      <stop offset="1" stop-color="#1c2029"/>
    </linearGradient>
  </defs>

  <!-- Open display folder -->
  <g class="folder-open">
    <path class="folder-flap-left" fill="url(#paper-sheen)" d="M476,464 C430,464 410,500 380,540 L380,800 C300,815 230,835 190,855 C160,870 145,883 145,893 L476,893 Z"/>
    <path class="folder-flap-right" fill="url(#flap-sheen)" d="M807,464 L1122,464 Q1136,464 1130,478 C1112,520 1066,560 1060,640 C1052,745 1000,850 930,893 L807,893 Z"/>
    <rect class="folder-inner-page" x="476" y="464" width="331" height="429" fill="url(#paper-sheen)"/>
    <path class="folder-pocket" fill="url(#obsidian-sheen)" d="M476,893 C496,800 560,723 660,723 L807,723 L807,893 Z"/>
    <g class="pocket-card">
      <rect x="637" y="772" width="131" height="86" rx="8" fill="url(#card-gloss)"/>
      <path d="M697,772 a6,6 0 0 0 12,0" fill="#07080f"/>
      <circle class="mark-dot" cx="702" cy="815" r="6"/>
      <text class="wordmark" x="702" y="843" font-size="6.5" text-anchor="middle">LEAF BY FROST</text>
    </g>
  </g>

  <!-- Folder front cover -->
  <g class="folder-cover-front">
    <rect x="55" y="391" width="326" height="428" fill="#0a0c16"/>
    <path fill="url(#slate-wave)" d="M55,391 C150,400 190,470 215,560 C245,680 290,790 381,819 L381,391 Z" transform="translate(0,0)"/>
    <path fill="#0a0c16" d="M55,391 C130,400 170,470 195,560 C225,680 265,790 340,819 L55,819 Z"/>
    <circle class="mark-dot" cx="112" cy="760" r="8"/>
    <text class="wordmark" x="112" y="789" font-size="5.5" text-anchor="middle">LEAF BY FROST</text>
  </g>

  <!-- Folder cover upright -->
  <g class="folder-cover-back">
    <rect x="398" y="22" width="331" height="428" fill="#0a0c16"/>
    <path fill="url(#slate-wave)" d="M398,22 L420,22 C480,40 520,130 545,240 C570,350 640,430 729,450 L398,450 Z"/>
    <circle class="mark-dot" cx="465" cy="380" r="8"/>
    <text class="wordmark" x="465" y="419" font-size="5.5" text-anchor="middle">LEAF BY FROST</text>
  </g>

  <!-- Letterhead -->
  <g class="letterhead">
    <rect x="749" y="20" width="332" height="430" fill="url(#paper-sheen)"/>
    <path fill="url(#obsidian-sheen)" d="M749,20 L806,20 Q824,20 824,38 L824,52 Q824,70 800,76 C772,82 756,88 749,98 Z"/>
    <circle class="mark-dot" cx="785" cy="38" r="5"/>
    <text class="wordmark" x="785" y="62" font-size="4" letter-spacing="1.5" text-anchor="middle">LEAF BY FROST</text>
    <text class="detail" x="760" y="86" font-size="4">7/18-20 HOLLIN AVE</text>
    <text class="detail" x="760" y="91" font-size="4">KELMORE NSW 2094</text>
    <text class="detail" x="760" y="97" font-size="4">ABN 52 804 319 246</text>
    <text class="web" x="760" y="106" font-size="4">WWW.LEAFBYFROST.EXAMPLE</text>
  </g>

  <!-- With compliments slip -->
  <g class="compliments-slip">
    <rect x="802" y="117" width="330" height="144" fill="url(#paper-sheen)"/>
    <path fill="url(#obsidian-sheen)" d="M802,117 L852,117 Q870,117 870,135 L870,146 Q870,164 846,170 C820,176 808,182 802,190 Z"/>
    <circle class="mark-dot" cx="836" cy="134" r="5"/>
    <text class="wordmark" x="836" y="155" font-size="4" letter-spacing="1.5" text-anchor="middle">LEAF BY FROST</text>
    <text class="detail" x="812" y="179" font-size="3.8">7/18-20 HOLLIN AVE</text>
    <text class="detail" x="812" y="184" font-size="3.8">KELMORE NSW 2094</text>
    <text class="detail" x="812" y="190" font-size="3.8">ABN 52 804 319 246</text>
    <text class="web" x="812" y="198" font-size="3.8">WWW.LEAFBYFROST.EXAMPLE</text>
  </g>

  <!-- Business card front -->
  <g class="business-card-front">
    <rect x="247" y="191" width="133" height="85" rx="8" fill="url(#card-gloss)"/>
    <circle class="mark-dot" cx="313" cy="223" r="8"/>
    <text class="wordmark" x="313" y="261" font-size="6" text-anchor="middle">LEAF BY FROST</text>
  </g>

  <!-- Business card back -->
  <g class="business-card-back">
    <rect x="247" y="288" width="133" height="86" rx="8" fill="url(#card-gloss)"/>
    <circle class="mark-dot" cx="285" cy="311" r="6"/>
    <text class="wordmark" x="285" y="334" font-size="3.8" letter-spacing="1.5" text-anchor="middle">LEAF BY FROST</text>
    <text class="holder-name" x="370" y="307" font-size="5" text-anchor="end">ROB K. DEVERILL</text>
    <text class="detail-light" x="370" y="313" font-size="3.2" text-anchor="end">PRODUCER</text>
    <text class="detail-light" x="285" y="343" font-size="3.4" text-anchor="middle">7/18-20 HOLLIN AVE</text>
    <text class="detail-light" x="285" y="347" font-size="3.4" text-anchor="middle">KELMORE NSW 2094</text>
    <text class="detail-light" x="285" y="352" font-size="3.4" text-anchor="middle">ABN 52 804 319 246</text>
    <text class="detail-light" x="370" y="358" font-size="3.6" text-anchor="end">T 0417 352 918</text>
    <text class="detail-light" x="370" y="364" font-size="3.6" text-anchor="end">E rob@leafbyfrost.example</text>
    <text class="web" x="259" y="365" font-size="3.6">WWW.LEAFBYFROST.EXAMPLE</text>
  </g>
</svg>
</body>
</html>
```